Ferris Contracting LLC Business Card Design

I am looking for a creative and unique business card design. We are a commercial construction general contractor. With the name "FERRIS" Contracting, I am hoping to see some neat designs that correlate with the name.

```html
<!DOCTYPE html>
<html lang="en">
<head>
<meta charset="UTF-8">
<title>Ferris Contracting LLC — Business Card</title>
<link href="https://fonts.googleapis.com/css2?family=Montserrat:wght@400;500;700;800&display=swap" rel="stylesheet">
<style>
  :root {
    --page-bg: #3a3a3a;
    --card-bg: #222223;
    --card-edge: #2b2b2c;
    --brand-blue: #1f8ad8;
    --text-light: #f2f2f2;
    --logo-grey: #4a4a4c;
    --ring-faint: #2d2d2f;
  }
  * { box-sizing: border-box; margin: 0; padding: 0; }
  html, body { width: 1200px; height: 875px; overflow: hidden; }
  body {
    background: var(--page-bg);
    font-family: "Montserrat", Arial, sans-serif;
    position: relative;
  }
  .card {
    position: absolute;
    left: 330px;
    width: 540px;
    height: 310px;
    background: var(--card-bg);
    border-radius: 18px;
    box-shadow: 0 10px 28px rgba(0,0,0,.35);
    overflow: hidden;
  }
  .card--back { top: 95px; display: flex; align-items: center; justify-content: center; }
  .card--front { top: 470px; }

  .wordmark {
    font-weight: 800;
    letter-spacing: 1px;
    line-height: 1;
    text-transform: uppercase;
  }
  .card--back .wordmark { color: var(--logo-grey); font-size: 52px; }
  .wordmark-sub { display: block; font-size: .32em; letter-spacing: 6px; margin-top: 6px; text-align: center; }

  .decor-ring {
    position: absolute;
    right: -30px;
    top: -40px;
    width: 280px;
    height: 280px;
    border-radius: 50%;
    border: 22px solid var(--ring-faint);
  }

  .front-logo {
    position: absolute;
    left: 34px;
    top: 30px;
    color: var(--brand-blue);
    font-size: 34px;
  }
  .details {
    position: absolute;
    left: 34px;
    top: 120px;
    color: var(--text-light);
    font-size: 12.5px;
    line-height: 1.45;
  }
  .person-name { color: var(--brand-blue); font-weight: 700; font-size: 21px; letter-spacing: .5px; line-height: 1.1; }
  .person-title { margin-bottom: 12px; font-size: 13px; }
  .address { margin-bottom: 12px; }
  .contact-list { list-style: none; }
  .contact-list li { display: flex; align-items: center; gap: 8px; }
  .contact-list svg { width: 11px; height: 11px; fill: var(--brand-blue); flex: none; }
</style>
</head>
<body>
  <section class="card card--back" aria-label="Card back">
    <div class="wordmark">Ferris<span class="wordmark-sub">Contracting</span></div>
  </section>

  <section class="card card--front" aria-label="Card front">
    <div class="decor-ring" aria-hidden="true"></div>
    <div class="wordmark front-logo">Ferris<span class="wordmark-sub">Contracting</span></div>
    <div class="details">
      <p class="person-name">DORIAN HALE</p>
      <p class="person-title">CEO/Founder</p>
      <p class="address">4170 Harbor Lane, Suite 212<br>Redwater, AB 55319</p>
      <ul class="contact-list">
        <li><svg viewBox="0 0 24 24"><path d="M6.6 10.8a15 15 0 0 0 6.6 6.6l2.2-2.2a1 1 0 0 1 1-.25 11.4 11.4 0 0 0 3.6.57 1 1 0 0 1 1 1V20a1 1 0 0 1-1 1A17 17 0 0 1 3 4a1 1 0 0 1 1-1h3.5a1 1 0 0 1 1 1c0 1.25.2 2.45.57 3.57a1 1 0 0 1-.25 1z"/></svg>(123)-555-0148</li>
        <li><svg viewBox="0 0 24 24"><path d="M2 5h20v14H2z M3.5 6.5 12 13l8.5-6.5" stroke="#222223" stroke-width="1.5"/></svg>info@ferriscontracting.com</li>
        <li><svg viewBox="0 0 24 24"><circle cx="12" cy="12" r="10"/></svg>www.ferriscontracting.com</li>
      </ul>
    </div>
  </section>
</body>
</html>
```